Premium Fitness Meal Plan Design for VoltaKor (Brand Like PlumQuarry!)

VoltaKor 6 Week Autumn Forge Meal Plan Design (Branded Handout)

πŸ“„ Overview:
We are looking for a professionally designed, branded meal plan handout for our fitness facility, VoltaKor. This meal plan will be used during our upcoming 6 Week Autumn Forge Quest, where members aim to lose body fat, build lean muscle, and improve their energy through nutrition and strength training.

The design should be highly polished, visually engaging, and reflect our brand quality β€” something on par with what you would see from larger national gym chains (e.g., Plum Quarry, K62, Delmar’s Drillyard). This is not just a text document β€” we want it to feel premium, motivating, and easy to follow, ideally something members are excited to reference and share.

🧾 Format & Layout:
Size: Standard 8.5x11 inch format (single or double-sided)

Final Output: Print-ready PDF + editable source files

Orientation: Portrait

Can be designed as either:

One visually organized front-and-back sheet

Or two clean, digestible pages presented as a mini-handout

🎨 Design Style:
Clean, energetic, and transformation-focused

Use brand colors and fonts that feel bold, fresh, and motivating

Include icons, dividers, or visual cues to separate sections (not just blocks of text)

Sections should feel approachable and empowering, not clinical or restrictive

Include room for the VoltaKor logo (provided) at the top and/or footer

πŸ“˜ Content to Include:
The following content should be visually structured and formatted in clear, engaging blocks. We’ll provide this content in a PDF format

1. Header Title:
"VoltaKor 6 Week Autumn Forge Nutrition Blueprint"

2. Introduction (Small Block):
Short blurb about the challenge goals (lose body fat, gain energy, preserve lean muscle mass)

3. Elimination List (Foods to Avoid):
A visually separated section with a list of foods and drinks that should be eliminated or greatly reduced for fat loss

4. Smart Swaps Table:
A side-by-side "Craving vs Swap" table that shows easy alternatives to popular bad habits (e.g., soda β†’ sparkling water)

5. Build-Your-Own Meal Plan Sections:
Organize these into clear categories:

Proteins

Carbs

Fats

Veggies

Extras / Smart Swaps
Use icons, color codes, or visual grids to organize these food lists

6. Tips Section (Optional Bonuses):
Hydration goal

Suggested number of meals

Protein shake recommendation

Meal timing tip

10-min walk after dinner tip

πŸ“¦ Files Provided:

All written content in organized text format

βœ… Deliverables:
Final design in print-ready PDF

Editable source file (AI, PSD, or InDesign preferred)

πŸ™Œ Inspiration:
Design should feel in line with the type of professional print materials used by high-end fitness studios. Clean lines, engaging fonts, and premium layout. We're not looking for clipart or gimmicky stock photos β€” we want the design to reflect the premium, results-driven experience our gym provides.

```html
<!DOCTYPE html>
<html lang="en">
<head>
<meta charset="utf-8">
<title>VoltaKor 6 Week Autumn Forge – Nutrition Blueprint</title>
<link rel="stylesheet" href="https://fonts.googleapis.com/css2?family=Cabin:wght@400;600;700&family=Oswald:wght@600;700&display=swap">
<style>
  :root{
    --ink:#111111;
    --black:#0a0a0b;
    --yellow:#f6cf12;
    --white:#ffffff;
    --backdrop:#a3a5aa;
    --photo-navy:#2c3452;
    --photo-slate:#5b6379;
  }
  *{box-sizing:border-box;margin:0;padding:0}
  html,body{width:1200px;height:822px;overflow:hidden;background:var(--backdrop)}
  body{position:relative;font-family:"Cabin",Arial,sans-serif;color:var(--ink)}
  .page{position:absolute;top:100px;width:481px;height:619px;background:var(--white);overflow:hidden}
  .page--front{left:105px}
  .page--back{left:613px}
  .abs{position:absolute}

  /* header */
  .hero{position:absolute;left:0;top:0;width:481px;height:232px}
  .hero-photo{position:absolute;left:0;top:0;width:481px;height:232px;
    background:linear-gradient(90deg,var(--black) 0%,var(--black) 38%,#1b2030 55%,var(--photo-navy) 72%,var(--photo-slate) 100%)}
  .hero-edge{position:absolute;left:0;top:195px}
  .brand{left:22px;top:18px;color:var(--white);font-weight:700;font-size:31px;letter-spacing:-.5px;line-height:1}
  .brand-tag{left:38px;top:53px;color:var(--yellow);font-size:5px;font-weight:700;letter-spacing:1px}
  .title{left:22px;top:66px;font-family:"Oswald",Impact,sans-serif;font-weight:700;font-size:29px;line-height:30.5px;letter-spacing:1px;color:var(--yellow)}
  .title .plain{color:var(--white)}
  .title-rule{left:22px;top:162px;width:229px;height:3px;background:var(--yellow)}
  .goal{left:22px;top:170px;width:320px;color:var(--white);font-size:8.3px;line-height:10.5px;letter-spacing:.2px}
  .goal b{color:var(--yellow)}

  /* section headings */
  .badge{position:absolute;width:28px;height:28px;border-radius:50%;background:var(--black);border:2px solid var(--yellow)}
  .badge::after{content:"";position:absolute;left:7px;top:7px;width:10px;height:10px;border:1.5px solid var(--yellow);border-radius:3px}
  .badge--sm{width:20px;height:20px;border-width:1.5px}
  .badge--sm::after{left:5px;top:5px;width:7px;height:7px;border-radius:2px}
  .sec-title{font-weight:700;font-size:10px;line-height:11px;letter-spacing:.1px}
  .sec-text{font-size:7.8px;line-height:9.2px}
  .list{list-style:none;font-size:7.8px;line-height:12.2px}
  .list li{position:relative;padding-left:9px}
  .list li::before{content:"";position:absolute;left:1px;top:5px;width:3.5px;height:3.5px;border-radius:50%;background:var(--ink)}
  .list--wide{line-height:13.7px}
  .list--wide li::before{top:5.5px}
  .list .cont{display:block}

  /* smart swaps */
  .swap-head{font-size:6.5px;font-weight:700;letter-spacing:.1px}
  .swap-head span{margin-left:6px}
  .swap-icon{left:280px}
  .swap-name{position:absolute;left:308px;font-size:9px;line-height:10px;font-weight:600;white-space:nowrap}
  .swap-desc{position:absolute;left:308px;width:152px;font-size:7.5px;line-height:9.2px}
  .swap-inline{font-size:7.8px;font-weight:400;margin-left:4px}

  .photo{position:absolute}

  /* back page */
  .back-top{position:absolute;left:0;top:0}
  .footer-band{position:absolute;left:0;top:505px}
  .contact{left:27px;top:548px;color:var(--white);font-size:9.4px;line-height:13.6px;letter-spacing:.3px}
  .contact-row{display:flex;align-items:center;gap:5px}
  .contact-row svg{flex:none}
</style>
</head>
<body>

<!-- FRONT PAGE -->
<section class="page page--front">
  <header class="hero">
    <div class="hero-photo" role="img" aria-label="Photo of a woman pressing dumbbells overhead in a gym, other members training behind her"></div>
    <svg class="hero-edge" width="481" height="40" viewBox="0 0 481 40" aria-hidden="true">
      <path d="M0 20 C60 14 110 16 170 12 C240 8 300 6 360 10 C410 12 450 16 481 20 L481 40 L0 40 Z" fill="#ffffff"/>
      <path d="M0 18 L40 17 L38 19 L90 16 M150 14 L220 11 M300 9 L330 10 M395 14 L470 18" stroke="#ffffff" stroke-width="1.2" fill="none"/>
    </svg>
    <div class="abs brand">VoltaKor</div>
    <div class="abs brand-tag">PERSONAL GROUP TRAINING</div>
    <h1 class="abs title">VOLTAKOR <span class="plain">6 WEEK AUTUMN</span><br>FORGE - NUTRITION<br>BLUEPRINT</h1>
    <div class="abs title-rule"></div>
    <p class="abs goal"><b>Goal:</b> Drop body fat, maintain lean muscle,<br>and boost energy — without giving up real food or living in the kitchen.</p>
  </header>

  <!-- eliminate -->
  <div class="badge" style="left:17px;top:232px"></div>
  <h2 class="abs sec-title" style="left:49px;top:235px">FOODS &amp; DRINKS TO ELIMINATE<br>(OR GREATLY REDUCE)</h2>
  <p class="abs sec-text" style="left:17px;top:265px;width:155px">These are the biggest culprits sabotaging fat loss — highly palatable, calorie-dense, and metabolically disruptive:</p>
  <ul class="abs list" style="left:17px;top:296px;width:262px">
    <li>Sugary drinks (sodas, energy drinks, sweet teas, juice blends)</li>
    <li>Fancy coffee drinks (Frostinos, sugary creamers, flavor pumps)</li>
    <li>Fast food and fried foods (even “grilled” items often packed with oils)</li>
    <li>Packaged snacks (chips, cookies, granola bars, trail mix with candy)</li>
    <li>Baked goods (donuts, muffins, pastries, bagels with cream cheese)</li>
    <li>Alcohol (especially beer and sugary mixers)</li>
    <li>Processed carbs (white breads, crackers, pasta)</li>
    <li>Cheese-heavy meals (pizza, nachos, quesadillas)</li>
    <li>High-fat deli meats (salami, pepperoni, sausage)</li>
    <li>Sauces and condiments loaded with sugar (ketchup, BBQ sauce, <span class="cont">honey mustard)</span></li>
  </ul>

  <svg class="photo" style="left:0;top:440px" width="270" height="179" viewBox="0 0 270 179" role="img" aria-label="Photo of a group fitness class doing kettlebell swings under colourful studio lights">
    <defs>
      <linearGradient id="classLight" x1="0" y1="0" x2="1" y2="1">
        <stop offset="0" stop-color="#3a2a5c"/>
        <stop offset=".5" stop-color="#7a3a6e"/>
        <stop offset="1" stop-color="#2a3c6a"/>
      </linearGradient>
    </defs>
    <path d="M0 4 C110 -6 240 50 262 179 L0 179 Z" fill="url(#classLight)"/>
    <path d="M20 1 C120 -2 235 50 258 179" stroke="#ffffff" stroke-width="3" fill="none"/>
  </svg>

  <!-- smart swaps -->
  <div class="badge" style="left:275px;top:232px"></div>
  <h2 class="abs sec-title" style="left:308px;top:240px">SMART SWAPS FOR FAT LOSS</h2>
  <p class="abs sec-text" style="left:308px;top:253px;width:152px">Instead of cutting everything and feeling deprived, make these easy grocery-store swaps that still satisfy cravings without killing your progress:</p>
  <div class="abs swap-head" style="left:308px;top:292px">Craving<span>Try This Instead</span></div>

  <div class="badge badge--sm swap-icon" style="top:297px"></div>
  <div class="swap-name" style="top:301px">Soda</div>
  <div class="swap-desc" style="top:311px">Sparkling water with lime, Zestra, or plain water with fruit infusions</div>

  <div class="badge badge--sm swap-icon" style="top:328px"></div>
  <div class="swap-name" style="top:333px">Fancy Coffee</div>
  <div class="swap-desc" style="top:343px">Coffee with unsweetened almond milk + stevia drops or cinnamon</div>

  <div class="badge badge--sm swap-icon" style="top:357px"></div>
  <div class="swap-name" style="top:362px">Chips</div>
  <div class="swap-desc" style="top:372px">Rice cakes, roasted chickpeas, or crunchy cucumber with Chilesal</div>

  <div class="badge badge--sm swap-icon" style="top:389px"></div>
  <div class="swap-name" style="top:393px">Ice Cream</div>
  <div class="swap-desc" style="top:403px">Frozen banana blended with protein powder (DIY "nice cream")</div>

  <div class="abs swap-head" style="left:308px;top:425px">Craving<span>Try This Instead</span></div>

  <div class="badge badge--sm swap-icon" style="top:433px"></div>
  <div class="swap-name" style="top:436px">Candy</div>
  <div class="swap-desc" style="top:446px">Berries, apples or dark chocolate squares (85%+)</div>

  <div class="badge badge--sm swap-icon" style="top:459px"></div>
  <div class="swap-name" style="top:466px">Pasta</div>
  <div class="swap-desc" style="top:476px">Zucchini noodles, chickpea pasta, or cauliflower rice</div>

  <div class="badge badge--sm swap-icon" style="top:490px"></div>
  <div class="swap-name" style="top:496px">Pizza</div>
  <div class="swap-desc" style="top:506px">Egg white wraps or low-carb tortillas with turkey pepperoni and light cheese</div>

  <div class="badge badge--sm swap-icon" style="top:516px"></div>
  <div class="swap-name" style="top:526px">Alcohol<span class="swap-inline">Limit to 1x/week if needed</span></div>

  <div class="badge badge--sm swap-icon" style="top:541px"></div>
  <div class="swap-name" style="top:542px">Sandwich Bread</div>
  <div class="swap-desc" style="top:552px">Sprouted grain bread, low-carb wraps, or lettuce wraps</div>

  <div class="badge badge--sm swap-icon" style="top:566px"></div>
  <div class="swap-name" style="top:573px">Heavy Sauces</div>
  <div class="swap-desc" style="top:583px">Mustard, salsa, hot sauce, coconut aminos, Greek yogurt-based dips</div>
</section>

<!-- BACK PAGE -->
<section class="page page--back">
  <svg class="back-top" width="481" height="16" viewBox="0 0 481 16" aria-hidden="true">
    <path d="M0 0 L481 0 L481 9 C400 11 300 7 200 10 C120 12 60 8 0 12 Z" fill="#0a0a0b"/>
    <path d="M10 13 L90 12 M140 12 L230 11" stroke="#0a0a0b" stroke-width="1" fill="none"/>
  </svg>

  <!-- left column -->
  <div class="badge" style="left:17px;top:21px"></div>
  <h2 class="abs sec-title" style="left:49px;top:28px">BUILD-YOUR-OWN MEAL PLAN GUIDE</h2>
  <p class="abs sec-text" style="left:49px;top:41px;width:180px">Use these fit-friendly food lists to mix &amp; match meals. Your job: choose 1 protein, 1 carb (if desired), and 1 fat or veggie at each meal. Keep it simple, keep it consistent.</p>

  <div class="badge" style="left:17px;top:85px"></div>
  <h2 class="abs sec-title" style="left:49px;top:91px">PROTEINS (choose 1 per meal/snack)</h2>
  <ul class="abs list" style="left:49px;top:104px;width:185px">
    <li>Chicken breast or thighs (air fried or grilled)</li>
    <li>Lean ground beef (90/10 or better)</li>
    <li>Ground turkey or turkey breast</li>
    <li>Center-cut pork chops</li>
    <li>Eggs / Egg whites</li>
    <li>Tuna (canned in water)</li>
    <li>Salmon or white fish</li>
    <li>Shrimp</li>
    <li>Greek yogurt (plain, low sugar)</li>
    <li>Cottage cheese (low-fat)</li>
    <li>Protein powder (whey or plant-based)</li>
    <li>Deli turkey (low-sodium)</li>
  </ul>

  <div class="badge" style="left:17px;top:258px"></div>
  <h2 class="abs sec-title" style="left:49px;top:264px">CARBS (choose 1–2 servings per day,<br>timed post-workout or morning)</h2>
  <ul class="abs list" style="left:49px;top:286px;width:185px">
    <li>Jasmine or basmati rice (white or brown)</li>
    <li>Sweet potatoes or yams</li>
    <li>Rolled oats or steel cut oats</li>
    <li>Quinoa</li>
    <li>Sprouted grain bread</li>
    <li>Rice cakes</li>
    <li>Berries (blueberries, raspberries, strawberries)</li>
    <li>Apples / Bananas</li>
    <li>Chickpeas or black beans (in moderation)</li>
  </ul>

  <div class="badge" style="left:17px;top:404px"></div>
  <h2 class="abs sec-title" style="left:49px;top:410px">FATS (add small amounts to meals,<br>2–4 servings/day)</h2>
  <ul class="abs list" style="left:49px;top:432px;width:185px">
    <li>Avocado or guacamole</li>
    <li>Olive oil or avocado oil (cooking or drizzle)</li>
    <li>Nut butters (almond, peanut – natural only)</li>
    <li>Whole eggs</li>
    <li>Nuts (almonds, walnuts – portion controlled)</li>
    <li>Chia seeds or flax seeds</li>
  </ul>

  <!-- right column -->
  <div class="badge" style="left:233px;top:21px"></div>
  <h2 class="abs sec-title" style="left:265px;top:28px">VEGGIES (unlimited – fill your plate!)</h2>
  <ul class="abs list list--wide" style="left:265px;top:40px;width:210px">
    <li>Spinach, kale, arugula</li>
    <li>Zucchini, asparagus, bell peppers</li>
    <li>Broccoli, cauliflower, green beans</li>
    <li>Cucumber, tomatoes, shredded carrots</li>
    <li>Mixed greens or salad kits (watch the dressing)</li>
  </ul>

  <div class="badge" style="left:233px;top:126px"></div>
  <h2 class="abs sec-title" style="left:265px;top:133px">BONUS TIPS FOR MAXIMUM RESULTS</h2>
  <ul class="abs list list--wide" style="left:265px;top:145px;width:212px">
    <li><b>Drink 80–120 oz. water daily</b><span class="cont">hydration is key for fat loss and muscle performance</span></li>
    <li><b>Eat 3–4 meals per day</b><span class="cont">spaced every 3–4 hours</span></li>
    <li><b>Include protein in every meal</b><span class="cont">to stabilize blood sugar and support muscle</span></li>
    <li><b>Post-workout meal = protein + carb,</b> no added fats</li>
    <li><b>Up to, two protein shakes per day is allowed,</b><span class="cont">especially post-workout or on busy days</span></li>
    <li><b>Limit “treat” meals to 1 per week</b> (keep it controlled)</li>
  </ul>

  <div class="badge" style="left:233px;top:299px"></div>
  <h2 class="abs sec-title" style="left:265px;top:306px">OPTIONAL HABITS TO STACK</h2>
  <ul class="abs list list--wide" style="left:265px;top:320px;width:210px">
    <li>Weigh in once per week (same day/time)</li>
    <li>Prep 2–3 proteins and veggies on Sunday</li>
    <li>Keep a visible “YES/NO” food list on the fridge</li>
    <li>Add a short 10-min walk after dinner to<span class="cont">boost digestion</span></li>
  </ul>

  <!-- footer -->
  <svg class="footer-band" width="481" height="114" viewBox="0 0 481 114" aria-hidden="true">
    <path d="M0 8 C80 4 160 6 240 2 L240 114 L0 114 Z" fill="#0a0a0b"/>
    <path d="M0 8 C70 4 150 5 240 1 L240 9 C150 12 70 10 0 14 Z" fill="#f6cf12"/>
    <path d="M0 14 L240 9 L240 114 L0 114 Z" fill="#0a0a0b"/>
  </svg>
  <svg class="photo" style="left:210px;top:400px" width="271" height="219" viewBox="0 0 271 219" role="img" aria-label="Photo of smiling gym members flexing together on the training floor">
    <defs>
      <linearGradient id="crewTone" x1="0" y1="0" x2="1" y2="1">
        <stop offset="0" stop-color="#2f6f9a"/>
        <stop offset=".55" stop-color="#5a3d8a"/>
        <stop offset="1" stop-color="#2b7a8c"/>
      </linearGradient>
    </defs>
    <path d="M271 6 L271 219 L10 219 C14 110 110 22 271 6 Z" fill="url(#crewTone)"/>
    <path d="M271 3 C110 18 10 110 6 219" stroke="#ffffff" stroke-width="3" fill="none"/>
  </svg>

  <div class="abs contact">
    <div class="contact-row"><svg width="8" height="8" viewBox="0 0 10 10" aria-hidden="true"><path d="M2 0.5 L4 0.5 L4.6 3 L3.3 4 C4 5.5 4.8 6.3 6 6.9 L7 5.6 L9.5 6.2 L9.5 8.2 C9.5 9 8.9 9.5 8 9.5 C4 9.2 0.8 6 0.5 2 C0.5 1 1 0.5 2 0.5 Z" fill="#f6cf12"/></svg>+1 555-014-2270</div>
    <div class="contact-row"><svg width="8" height="8" viewBox="0 0 10 10" aria-hidden="true"><rect x="0.7" y="2" width="8.6" height="6.2" fill="none" stroke="#f6cf12" stroke-width="1"/><path d="M0.7 2 L5 5.5 L9.3 2" fill="none" stroke="#f6cf12" stroke-width="1"/></svg>hello@voltakor.example</div>
    <div class="contact-row"><svg width="8" height="8" viewBox="0 0 10 10" aria-hidden="true"><circle cx="5" cy="5" r="4.3" fill="none" stroke="#f6cf12" stroke-width="1"/><ellipse cx="5" cy="5" rx="1.9" ry="4.3" fill="none" stroke="#f6cf12" stroke-width=".8"/><path d="M0.7 5 H9.3" stroke="#f6cf12" stroke-width=".8"/></svg>www.joinvoltakor.example/strategy_session</div>
  </div>
</section>

</body>
</html>
```